Professional Corporate Business Card and Stationery Design for Freight Trucking Transportation Co.
Peter R. Malloy General Manager
Professional Corporate Business Card and Stationery Design for Freight Trucking Transportation Co. - Transportation
Creative Brief
Professional
Peter R. Malloy
V.P. of Operations / General Manager
7-48213 Upper Greyling Ridge Road Abbotsford, B.C. V2K4N7 Canada
HarrowTrans@pelvane.ca
This design project is for Business Cards and Business Stationey Harrow Transportation and Logistics Ltd. is a professional freight truck transport carrier based out of British Columbia, Canada. We provide highly crafted cargo delivery platforms to premier shippers of commodities throughout the five border Provinces of Canada and the Lower 48 United States of America. We are a "For-Hire" Motor Carrier which hauls shipper commodities from points within Canada to points within Canada and to points in the USA. We also transport freight from the United States into points within Canada. Threfore, we pride ourselves on superior performance and service, second to none in trucking freight industry. The above link will take you to what we feel is a example set of very highly crafted, upscale imagery designs created by artists on this very site and exemplifies the grit and character of true, quality Business card and Stationery designs, representation of the values of business professionalism we stand for and wish to convey in our stationery and other designs. Are you challenged enough to join in the fray and craft a unique design which can stand on par with those on this link? Today is April 25, 2014 - The challenge is to wow not only Harrow, but yourselves and your peers... ??
Harrow Harrow

```html
<!DOCTYPE html>
<html lang="en">
<head>
<meta charset="utf-8">
<title>Harrow Transportation and Logistics — Business Card</title>
<link rel="stylesheet" href="https://fonts.googleapis.com/css2?family=Montserrat:wght@400;500;700&family=Raleway:wght@400;500&display=swap">
<style>
  :root {
    --backdrop: #d9d9db;
    --card: #ffffff;
    --ink: #2b2b2b;
    --ink-soft: #6a6a6a;
    --black: #141414;
    --red: #c4161c;
    --name-light: #f2f2f2;
  }
  * { margin: 0; padding: 0; box-sizing: border-box; }
  html, body { width: 1200px; height: 653px; overflow: hidden; }
  body {
    background: var(--backdrop);
    font-family: "Montserrat", sans-serif;
    position: relative;
  }
  .card {
    position: absolute;
    width: 540px;
    height: 309px;
    background: var(--card);
    box-shadow: 0 10px 28px rgba(0,0,0,.18);
    overflow: hidden;
  }
  .card--front { left: 45px; top: 172px; }
  .card--back { left: 615px; top: 172px; }

  .brand {
    position: absolute;
    display: flex;
    align-items: center;
    gap: 10px;
  }
  .brand__dot {
    width: 22px; height: 22px;
    border-radius: 50%;
    background: var(--red);
  }
  .brand__name {
    font-family: "Montserrat", sans-serif;
    font-weight: 700;
    font-size: 30px;
    letter-spacing: 3px;
    text-transform: uppercase;
    color: var(--ink);
  }
  .card--front .brand { left: 50%; top: 50%; transform: translate(-50%, -50%); }
  .card--back .brand { left: 188px; top: 62px; }
  .card--back .brand__name { font-size: 24px; letter-spacing: 2px; }
  .card--back .brand__dot { width: 18px; height: 18px; }

  .swoosh { position: absolute; inset: 0; width: 100%; height: 100%; }

  .contact {
    position: absolute;
    right: 26px;
    top: 48px;
    list-style: none;
    text-align: right;
    font-family: "Raleway", sans-serif;
    font-size: 9.5px;
    line-height: 1.75;
    color: var(--ink-soft);
  }
  .contact__item { display: flex; justify-content: flex-end; align-items: center; gap: 6px; }
  .contact__gap { margin-top: 10px; }
  .contact__icon { width: 9px; height: 9px; fill: var(--ink-soft); }

  .person {
    position: absolute;
    left: 26px;
    bottom: 36px;
    color: var(--name-light);
  }
  .person__name {
    font-family: "Raleway", sans-serif;
    font-weight: 500;
    font-size: 15px;
    letter-spacing: 2px;
    text-transform: uppercase;
  }
  .person__title {
    font-size: 8.5px;
    letter-spacing: 1px;
    color: #a9a9a9;
    margin-top: 4px;
  }
</style>
</head>
<body>

  <section class="card card--front" aria-label="Card front">
    <div class="brand">
      <span class="brand__dot"></span>
      <span class="brand__name">Harrow</span>
    </div>
  </section>

  <section class="card card--back" aria-label="Card back">
    <svg class="swoosh" viewBox="0 0 540 309" preserveAspectRatio="none" aria-hidden="true">
      <path d="M0,0 L62,0 C95,170 220,290 380,309 L0,309 Z" fill="var(--black)"/>
      <path d="M62,0 L74,0 C108,160 228,278 380,309 C220,290 95,170 62,0 Z" fill="var(--red)"/>
      <path d="M74,0 L80,0 C114,150 236,270 400,309 L380,309 C228,278 108,160 74,0 Z" fill="#ffffff"/>
      <path d="M110,8 C160,0 200,6 215,14" fill="none" stroke="var(--red)" stroke-width="0"/>
    </svg>

    <div class="brand">
      <span class="brand__dot"></span>
      <span class="brand__name">Harrow</span>
    </div>

    <ul class="contact">
      <li class="contact__item">7-48213 Upper Greyling Ridge Road</li>
      <li class="contact__item">Abbotsford, B.C. V2K4N7</li>
      <li class="contact__item contact__gap">604 555 0142
        <svg class="contact__icon" viewBox="0 0 10 10"><path d="M2 0.5 L3.8 2.6 L2.9 3.8 C3.6 5.2 4.8 6.4 6.2 7.1 L7.4 6.2 L9.5 8 L8.4 9.5 C4.5 9.3 0.7 5.5 0.5 1.6 Z"/></svg>
      </li>
      <li class="contact__item">604 555 0187
        <svg class="contact__icon" viewBox="0 0 10 10"><path d="M2 0.5 L3.8 2.6 L2.9 3.8 C3.6 5.2 4.8 6.4 6.2 7.1 L7.4 6.2 L9.5 8 L8.4 9.5 C4.5 9.3 0.7 5.5 0.5 1.6 Z"/></svg>
      </li>
      <li class="contact__item">HarrowTrans@pelvane.ca
        <svg class="contact__icon" viewBox="0 0 10 10"><path d="M0.5 2 H9.5 V8 H0.5 Z M0.5 2 L5 5.5 L9.5 2" fill="none" stroke="#6a6a6a" stroke-width="1"/></svg>
      </li>
      <li class="contact__item">www.harrowtrans.ca
        <svg class="contact__icon" viewBox="0 0 10 10"><circle cx="5" cy="5" r="4.2" fill="none" stroke="#6a6a6a" stroke-width="1"/><path d="M0.8 5 H9.2 M5 0.8 C2.5 3.5 2.5 6.5 5 9.2 M5 0.8 C7.5 3.5 7.5 6.5 5 9.2" fill="none" stroke="#6a6a6a" stroke-width=".8"/></svg>
      </li>
    </ul>

    <div class="person">
      <p class="person__name">Peter R. Malloy</p>
      <p class="person__title">General Manager</p>
    </div>
  </section>

</body>
</html>
```